Honey Labels- Brambleview Seasonal Honey

I need to make three labels for my Brambleview Honey.

The honey is made by rescued honey bees in the City of Toronto. The bees are rescued by Hollowmere Hive Shelter. We harvest are honey based on season so that you can taste the different flavours of the seasons.

The three honeys that we sell are:
Brambleview Spring Blossom
Brambleview Summer Blossom
Brambleview Fall Blossom

The label is for a 500g bottle. Label size is 4 inches wide X 3 inches tall

Target Market(s)

Foodies who will pay a premium
Torontonians who want hyper local products
Tourists
Supporters of social coauses

Industry/Entity Type

Food Store

Requirements
Must have
• Must highlight the work Hollowmere hive shelter does
• Showcase that it is urban honey
• Differentiate between the seasons (spring. summer, fall)
Nice to have
• visual depiction of seasons
Should not have
• dark colours

```html
<!DOCTYPE html>
<html lang="en">
<head>
<meta charset="utf-8">
<title>Brambleview Seasonal Honey – Labels</title>
<link rel="stylesheet" href="https://fonts.googleapis.com/css2?family=Indie+Flower&family=Oswald:wght@300;600&family=Arimo:wght@400;700&display=swap">
<style>
  :root {
    --page: #ffffff;
    --label-edge: #d8c7ae;
    --label-mid: #f3eee7;
    --honey-type: #c27d2c;
    --ink: #2b2622;
    --band: #27221e;
    --band-text: #e8dcc4;
    --gold: #e6b00f;
    --scene-top: #c9c6c2;
    --scene-bottom: #9f9c98;
    --spring: #72a83a;
    --summer: #1f6a2c;
    --fall: #d98a2b;
  }
  * { box-sizing: border-box; margin: 0; padding: 0; }
  html, body { width: 1200px; height: 1200px; overflow: hidden; background: var(--page); }
  .label-set {
    position: relative; width: 1200px; height: 1200px;
    display: flex; justify-content: center; align-items: center; gap: 30px;
  }
  .label {
    position: relative; width: 360px; height: 270px; overflow: hidden;
    background: linear-gradient(90deg, var(--label-edge) 0%, var(--label-mid) 45%, var(--label-mid) 60%, var(--label-edge) 100%);
  }
  .label--spring { --season: var(--spring); }
  .label--summer { --season: var(--summer); }
  .label--fall { --season: var(--fall); }
  .season-corner { position: absolute; left: 0; top: 0; width: 110px; height: 100px; }
  .season-corner polygon { fill: var(--season); }
  .variety {
    position: absolute; left: 100px; top: 32px;
    font: 400 19px/1 'Indie Flower', cursive; color: var(--season); white-space: nowrap;
  }
  .product-type {
    position: absolute; left: 104px; top: 68px;
    font: 300 40px/1 'Oswald', sans-serif; color: var(--honey-type);
    letter-spacing: 1px; transform: scaleY(1.15); transform-origin: top left;
  }
  .city-scene {
    position: absolute; left: 0; top: 124px; width: 215px; height: 58px;
    background: linear-gradient(180deg, var(--scene-top) 0%, var(--scene-bottom) 100%);
    opacity: .85;
  }
  .shelter-name {
    position: absolute; left: 10px; top: 190px;
    display: flex; align-items: center; gap: 6px;
    font: 600 19px/1 'Oswald', sans-serif; color: var(--ink); white-space: nowrap;
  }
  .shelter-name .dot { width: 12px; height: 12px; border-radius: 50%; background: var(--gold); }
  .nutrition {
    position: absolute; left: 233px; top: 80px; width: 116px; height: 146px;
    border: 1px solid var(--ink); background: #fbf9f6; padding: 3px 4px;
    font: 400 5px/1.25 'Arimo', sans-serif; color: var(--ink);
  }
  .nutrition h3 { font: 700 8.5px/1 'Arimo', sans-serif; letter-spacing: .3px; }
  .nutrition .serving { margin-top: 1px; border-bottom: 3px solid var(--ink); padding-bottom: 2px; }
  .nutrition .row { display: flex; justify-content: space-between; border-bottom: .5px solid var(--ink); padding: 1px 0; }
  .nutrition .row b { font-weight: 700; }
  .nutrition .row.thick { border-bottom-width: 2px; }
  .nutrition .indent { padding-left: 6px; }
  .nutrition .note { margin-top: 3px; font-size: 4px; line-height: 1.3; }
  .bottom-band {
    position: absolute; left: 0; bottom: 0; width: 100%; height: 34px;
    background: var(--band); border-top: 2px solid var(--gold);
    display: flex; justify-content: space-between; align-items: center; padding: 0 30px 0 45px;
    font: 400 15px/1 'Indie Flower', cursive; color: var(--band-text);
  }
</style>
</head>
<body>
<main class="label-set">

  <article class="label label--spring">
    <svg class="season-corner" viewBox="0 0 110 100" aria-hidden="true"><polygon points="0,0 110,0 0,100"/></svg>
    <p class="variety">Brambleview Spring Blossom</p>
    <h2 class="product-type">HONEY</h2>
    <div class="city-scene" role="img" aria-label="City skyline silhouette with a honey bee"></div>
    <p class="shelter-name"><span class="dot"></span>Hollowmere Hive Shelter</p>
    <section class="nutrition">
      <h3>Nutrition Facts<br>Valeur nutritive</h3>
      <p class="serving">Per 1 tablespoon (20g)<br>Pour 1 cuillère à table (20g)</p>
      <div class="row"><span>Amount<br>Teneur</span><span>% Daily Value<br>% valeur quotidienne</span></div>
      <div class="row thick"><b>Calories / Calories 60</b></div>
      <div class="row"><span><b>Fat / Lipides</b> 0 g</span><span>0 %</span></div>
      <div class="row"><span><b>Carbohydrates / Glucides</b> 17 g</span><span>6 %</span></div>
      <div class="row indent"><span>Sugars / Sucres 16 g</span></div>
      <div class="row thick"><span><b>Protein / Protéines</b> 0 g</span></div>
      <p class="note">Not a significant source of saturated fat, trans fat, cholesterol, sodium, fibre, vitamin A, vitamin C, calcium or iron.</p>
      <p class="note">Source négligeable de lipides saturés, lipides trans, cholestérol, sodium, fibres, vitamine A, vitamine C, calcium et fer.</p>
    </section>
    <footer class="bottom-band"><span>Product of Canada</span><span>500gr</span></footer>
  </article>

  <article class="label label--summer">
    <svg class="season-corner" viewBox="0 0 110 100" aria-hidden="true"><polygon points="0,0 110,0 0,100"/></svg>
    <p class="variety">Brambleview Summer Blossom</p>
    <h2 class="product-type">HONEY</h2>
    <div class="city-scene" role="img" aria-label="City skyline silhouette with a honey bee"></div>
    <p class="shelter-name"><span class="dot"></span>Hollowmere Hive Shelter</p>
    <section class="nutrition">
      <h3>Nutrition Facts<br>Valeur nutritive</h3>
      <p class="serving">Per 1 tablespoon (20g)<br>Pour 1 cuillère à table (20g)</p>
      <div class="row"><span>Amount<br>Teneur</span><span>% Daily Value<br>% valeur quotidienne</span></div>
      <div class="row thick"><b>Calories / Calories 60</b></div>
      <div class="row"><span><b>Fat / Lipides</b> 0 g</span><span>0 %</span></div>
      <div class="row"><span><b>Carbohydrates / Glucides</b> 17 g</span><span>6 %</span></div>
      <div class="row indent"><span>Sugars / Sucres 16 g</span></div>
      <div class="row thick"><span><b>Protein / Protéines</b> 0 g</span></div>
      <p class="note">Not a significant source of saturated fat, trans fat, cholesterol, sodium, fibre, vitamin A, vitamin C, calcium or iron.</p>
      <p class="note">Source négligeable de lipides saturés, lipides trans, cholestérol, sodium, fibres, vitamine A, vitamine C, calcium et fer.</p>
    </section>
    <footer class="bottom-band"><span>Product of Canada</span><span>500gr</span></footer>
  </article>

  <article class="label label--fall">
    <svg class="season-corner" viewBox="0 0 110 100" aria-hidden="true"><polygon points="0,0 110,0 0,100"/></svg>
    <p class="variety">Brambleview Fall Blossom</p>
    <h2 class="product-type">HONEY</h2>
    <div class="city-scene" role="img" aria-label="City skyline silhouette with a honey bee"></div>
    <p class="shelter-name"><span class="dot"></span>Hollowmere Hive Shelter</p>
    <section class="nutrition">
      <h3>Nutrition Facts<br>Valeur nutritive</h3>
      <p class="serving">Per 1 tablespoon (20g)<br>Pour 1 cuillère à table (20g)</p>
      <div class="row"><span>Amount<br>Teneur</span><span>% Daily Value<br>% valeur quotidienne</span></div>
      <div class="row thick"><b>Calories / Calories 60</b></div>
      <div class="row"><span><b>Fat / Lipides</b> 0 g</span><span>0 %</span></div>
      <div class="row"><span><b>Carbohydrates / Glucides</b> 17 g</span><span>6 %</span></div>
      <div class="row indent"><span>Sugars / Sucres 16 g</span></div>
      <div class="row thick"><span><b>Protein / Protéines</b> 0 g</span></div>
      <p class="note">Not a significant source of saturated fat, trans fat, cholesterol, sodium, fibre, vitamin A, vitamin C, calcium or iron.</p>
      <p class="note">Source négligeable de lipides saturés, lipides trans, cholestérol, sodium, fibres, vitamine A, vitamine C, calcium et fer.</p>
    </section>
    <footer class="bottom-band"><span>Product of Canada</span><span>500gr</span></footer>
  </article>

</main>
</body>
</html>
```